Business Card and Letterhead Design for Public Accounting Firm

Business card and letterhead design for a CPA Firm located in Orange County, CA. We're looking for a modern and professional design utilizing our existing logo. We'd like a clean "less is more" look, but also something that catches the eye. We provide a high level of service to our clients. Open to single or double sided business cards.

Additional info: color numbers on logo
Blue :
R 0
G 83
B 125

#00537D

Silver :

R 154
G 154
B 154

#9A9A9A

Target Market(s)

Businesses and individuals

Industry/Entity Type

Accounting

Contact Information for Business Card

Hewitt Dansby & Mortlake LLP - 4726 Larkspur Hollow Road, Irvine, CA 92614 - (949)382-7146 - hdmledgers.example

Font styles to use
Serif
Sans Serif
Other font styles liked:
• See font file uploaded

Colors
0054AA
0677BA
7BADD7
CADEEF
E8F1F8

Requirements
Nice to have
• Possibly use the font file provided which matches our logo, but adjust to be not in all caps

```html
<!DOCTYPE html>
<html lang="en">
<head>
<meta charset="utf-8">
<title>Hewitt Dansby &amp; Mortlake LLP – Stationery</title>
<link href="https://fonts.googleapis.com/css2?family=Open+Sans:wght@400;600&family=Roboto:wght@400;500;700&display=swap" rel="stylesheet">
<style>
  :root{
    --brand-blue:#00537D;
    --brand-silver:#9A9A9A;
    --ink:#555a5e;
    --paper:#ffffff;
    --backdrop:#e4e7e7;
    --photo-dark:#1d3550;
    --photo-mid:#6d7f92;
    --photo-light:#c9cfd4;
  }
  *{box-sizing:border-box;margin:0;padding:0}
  html,body{width:1200px;height:900px;overflow:hidden}
  body{background:var(--backdrop);position:relative;font-family:"Roboto",sans-serif;color:var(--ink)}
  .sheet{position:absolute;background:var(--paper);box-shadow:0 6px 18px rgba(0,0,0,.12)}
  .firm-name{font-family:"Roboto",sans-serif;font-weight:500;color:var(--brand-blue);letter-spacing:.02em}
  .icon{width:9px;height:9px;vertical-align:-1px;margin-right:3px;fill:var(--brand-blue)}

  /* business cards */
  .card{width:300px;height:170px}
  .card--front{left:40px;top:130px;padding:22px 22px}
  .card__brand{position:absolute;right:20px;top:22px;font-size:11px;width:130px;text-align:right;line-height:1.3}
  .card__person{font-weight:700;font-size:12px;color:var(--brand-blue);text-transform:uppercase;margin-top:14px}
  .card__role{font-size:9px;margin-bottom:8px}
  .card__contact{font-size:9px;line-height:1.6}
  .card__rule{position:absolute;left:150px;right:20px;top:72px;border-top:1px solid var(--brand-silver)}
  .card__address{position:absolute;right:20px;bottom:18px;text-align:right;font-size:8.5px;line-height:1.45}
  .card--back{left:40px;top:330px;background:var(--brand-blue);display:flex;align-items:center;justify-content:center}
  .card__brand--reverse{color:#ffffff;font-size:16px;text-align:center;line-height:1.35}

  /* letterhead */
  .letterhead{left:380px;top:40px;width:400px;height:566px;padding:34px 40px 24px}
  .letterhead__brand{display:block;text-align:right;font-size:13px;margin-bottom:26px}
  .letter{font-family:"Open Sans",sans-serif;font-size:7.4px;line-height:1.5;color:#6a6e72}
  .letter p{margin-bottom:8px}
  .letter__signature{width:60px;height:26px;background:#d7dde4;margin-top:4px}
  .letterhead__footer{position:absolute;left:40px;right:40px;bottom:30px;font-size:8px;line-height:1.6}
  .letterhead__footer-name{font-size:9px}

  /* envelope */
  .envelope{left:380px;top:640px;width:460px;height:230px}
  .envelope__brand{position:absolute;left:150px;top:26px;font-size:13px}
  .envelope__address{position:absolute;left:40px;top:120px;font-size:11px;line-height:1.4}
  .envelope__address-name{font-size:12px}
  .envelope__window{position:absolute;right:40px;bottom:26px;width:130px;height:66px;border:1px solid #d4d6d8;border-radius:8px;background:linear-gradient(135deg,#f7f7f7,#ececec)}

  /* presentation folder */
  .folder{left:830px;top:70px;width:340px;height:500px}
  .folder__brand{position:absolute;right:24px;top:44px;font-size:15px;text-align:right;line-height:1.35}
  .folder__photo{position:absolute;left:0;right:0;top:118px;height:220px;background:linear-gradient(110deg,var(--photo-dark) 0%,var(--photo-mid) 45%,var(--photo-light) 60%,var(--photo-dark) 100%)}
  .folder__address{position:absolute;left:0;right:0;top:376px;text-align:center;font-size:14px;line-height:1.4}
  .folder__address-name{display:block;font-size:16px}
</style>
</head>
<body>

<svg width="0" height="0" style="position:absolute">
  <symbol id="i-phone" viewBox="0 0 10 10"><path d="M2 0.5l1.6 2-1 1c.6 1.3 1.6 2.3 2.9 2.9l1-1 2 1.6-.9 1.9C4.5 9.3.7 5.5.1 1.4z"/></symbol>
  <symbol id="i-mail" viewBox="0 0 10 10"><path d="M0 2h10v6H0z M0 2l5 3.5L10 2" stroke="#fff" stroke-width=".8"/></symbol>
  <symbol id="i-web" viewBox="0 0 10 10"><circle cx="5" cy="5" r="4.6"/><path d="M.5 5h9M5 .5v9" stroke="#fff" stroke-width=".7"/></symbol>
</svg>

<!-- business card, front -->
<section class="sheet card card--front">
  <span class="firm-name card__brand">Hewitt Dansby &amp; Mortlake LLP</span>
  <p class="card__person">Tobias R. Lindqvist</p>
  <p class="card__role">Founder &amp; CEO</p>
  <p class="card__contact"><svg class="icon"><use href="#i-phone"/></svg>(949)382-7146</p>
  <p class="card__contact"><svg class="icon"><use href="#i-mail"/></svg>info@hdmledgers.example</p>
  <p class="card__contact"><svg class="icon"><use href="#i-web"/></svg>www.hdmledgers.example</p>
  <div class="card__rule"></div>
  <p class="card__address">Hewitt Dansby &amp; Mortlake LLP<br>4726 Larkspur Hollow Road,<br>Irvine, CA 92614</p>
</section>

<!-- business card, back -->
<section class="sheet card card--back">
  <span class="firm-name card__brand--reverse">Hewitt Dansby<br>&amp; Mortlake LLP</span>
</section>

<!-- letterhead -->
<section class="sheet letterhead">
  <span class="firm-name letterhead__brand">Hewitt Dansby &amp; Mortlake LLP</span>
  <div class="letter">
    <p>Dear customer,</p>
    <p>Lorem ipsum dolor sit amet, consectetur adipisicing elit, sed do eiusmod tempor incididunt ut labore et dolore magna aliqua. Ut enim ad minim veniam, quis nostrud exercitation ullamco laboris nisi ut aliquip ex ea commodo consequat. Duis aute irure dolor in reprehenderit in voluptate velit esse cillum dolore eu fugiat nulla pariatur. Excepteur sint occaecat cupidatat non proident, sunt in culpa qui officia deserunt mollit anim id est laborum.</p>
    <p>Lorem ipsum dolor sit amet, consectetur adipisicing elit, sed do eiusmod tempor incididunt ut labore et dolore magna aliqua. Ut enim ad minim veniam, quis nostrud exercitation ullamco laboris nisi ut aliquip ex ea commodo consequat. Duis aute irure dolor in reprehenderit in voluptate velit esse cillum dolore eu fugiat nulla pariatur. Excepteur sint occaecat cupidatat non proident, sunt in culpa qui officia deserunt mollit anim id est laborum.</p>
    <p>Lorem ipsum dolor sit amet, consectetur adipisicing elit, sed do eiusmod tempor incididunt ut labore et dolore magna aliqua. Ut enim ad minim veniam, quis nostrud exercitation ullamco laboris nisi ut aliquip ex ea commodo consequat. Duis aute irure dolor in reprehenderit in voluptate velit esse cillum dolore eu fugiat nulla pariatur. Excepteur sint occaecat cupidatat non proident, sunt in culpa qui officia deserunt mollit anim id est laborum.</p>
    <p>Lorem ipsum dolor sit amet, consectetur adipisicing elit, sed do eiusmod tempor incididunt ut labore et dolore magna aliqua. Ut enim ad minim veniam, quis nostrud exercitation ullamco laboris nisi ut aliquip ex ea commodo consequat. Duis aute irure dolor in reprehenderit.</p>
    <p>Yours Sincerely,</p>
    <div class="letter__signature" role="img" aria-label="Handwritten signature"></div>
  </div>
  <footer class="letterhead__footer">
    <span class="firm-name letterhead__footer-name">Hewitt Dansby &amp; Mortlake LLP</span><br>
    4726 Larkspur Hollow Road, Irvine, CA 92614<br>
    <svg class="icon"><use href="#i-phone"/></svg>(949)382-7146&nbsp;&nbsp;
    <svg class="icon"><use href="#i-mail"/></svg>info@hdmledgers.example&nbsp;&nbsp;
    <svg class="icon"><use href="#i-web"/></svg>www.hdmledgers.example
  </footer>
</section>

<!-- envelope -->
<section class="sheet envelope">
  <span class="firm-name envelope__brand">Hewitt Dansby &amp; Mortlake LLP</span>
  <p class="envelope__address"><span class="firm-name envelope__address-name">Hewitt Dansby &amp; Mortlake LLP</span><br>4726 Larkspur Hollow Road,<br>Irvine, CA 92614</p>
  <div class="envelope__window"></div>
</section>

<!-- presentation folder -->
<section class="sheet folder">
  <span class="firm-name folder__brand">Hewitt Dansby<br>&amp; Mortlake LLP</span>
  <div class="folder__photo" role="img" aria-label="Photograph of colleagues in a business meeting"></div>
  <p class="folder__address"><span class="firm-name folder__address-name">Hewitt Dansby &amp; Mortlake LLP</span>4726 Larkspur Hollow Road,<br>Irvine, CA 92614</p>
</section>

</body>
</html>
```